Verdant Orchard - Stationery Design Project

We need a stationary for our business. We grow roots and fruits in Central and South America, we import and distribute in FL, USA. We do fresh and frozen products.

Target Market(s)

Small and big supermarkets, wholesalers, traders, distributors, etc

Industry/Entity Type

Business

```html
<!DOCTYPE html>
<html lang="en">
<head>
<meta charset="utf-8">
<title>Verdant Orchard – Stationery</title>
<link rel="stylesheet" href="https://fonts.googleapis.com/css2?family=Open+Sans:wght@400;600&family=Tinos:ital@0;1&display=swap">
<style>
  :root {
    --olive: #566636;
    --orange: #e5831a;
    --orange-soft: #f0b77a;
    --paper: #ffffff;
    --ground: #ebebeb;
    --ink: #1e1e1e;
    --muted: #555555;
  }
  * { margin: 0; padding: 0; box-sizing: border-box; }
  html, body { width: 1200px; height: 1000px; overflow: hidden; }
  body { background: var(--ground); position: relative; font-family: "Open Sans", Arial, sans-serif; }

  .brand-name { font-family: "Open Sans", Arial, sans-serif; font-weight: 600; color: var(--orange); letter-spacing: 0.02em; white-space: nowrap; }

  /* Letterhead */
  .letterhead { position: absolute; left: 85px; top: 75px; width: 602px; height: 850px; background: var(--paper); overflow: hidden; }
  .letterhead .brand-name { position: absolute; top: 66px; left: 0; width: 100%; text-align: center; font-size: 20px; }
  .letter { position: absolute; left: 78px; top: 187px; width: 450px; font-family: "Tinos", "Times New Roman", serif; font-size: 12.6px; line-height: 15.6px; color: var(--ink); }
  .letter p { text-align: justify; margin-bottom: 15.6px; }
  .letter .closing { margin-top: 46px; margin-bottom: 0; text-align: left; }
  .signature { display: block; width: 110px; height: 32px; background: #e4e4e4; margin: 2px 0 4px; }
  .letter .signer { text-align: left; }
  .letter-contact { position: absolute; left: 74px; top: 752px; font-size: 6.6px; color: var(--muted); line-height: 10.6px; }
  .letter-contact .address { margin-bottom: 5px; }
  .letter-contact li { list-style: none; display: flex; align-items: center; gap: 8px; }
  .letter-contact svg { width: 7px; height: 7px; fill: var(--orange); }

  /* Cards */
  .card { position: absolute; left: 723px; width: 387px; height: 215px; background: var(--paper); overflow: hidden; }
  .card-front { top: 75px; }
  .card-front .brand-name { position: absolute; top: 96px; width: 100%; text-align: center; font-size: 24px; }
  .card-front .web { position: absolute; top: 144px; width: 100%; text-align: center; font-size: 13px; color: var(--olive); letter-spacing: 0.03em; }

  .card-back { top: 318px; }
  .card-back .brand-name { position: absolute; left: 27px; top: 38px; font-size: 17px; }
  .card-back .wave { position: absolute; left: 0; top: 0; width: 387px; height: 215px; }
  .card-back .person { position: absolute; left: 31px; top: 158px; color: #fff; }
  .card-back .person .name { font-size: 13px; letter-spacing: 0.02em; }
  .card-back .person .role { font-size: 7px; color: var(--orange); margin-top: 3px; }
  .card-back .address { position: absolute; right: 22px; top: 127px; font-size: 7.4px; color: #fff; }
  .card-back .contacts { position: absolute; right: 22px; top: 145px; font-size: 7.6px; color: #fff; line-height: 13.4px; text-align: right; }
  .card-back .contacts li { list-style: none; display: flex; justify-content: flex-end; align-items: center; gap: 9px; }
  .card-back .contacts svg { width: 7px; height: 7px; fill: var(--orange); }
</style>
</head>
<body>

<section class="letterhead">
  <div class="brand-name">Verdant Orchard</div>

  <div class="letter">
    <p style="margin-bottom:15.6px">Gentlemen,</p>
    <p>Enclosed I have the honor to send you an article which I should be pleased if you would accept for the "Evening Ledger". I am <i>desperately</i> pushed for money; and in the event of Mr. Hallam's liking the "Landscape-Garden", I would take it as an especial favor if you would mail me the amount due for it, so as to reach me here by the 21st, on which day I shall need it. Can you possibly oblige me in this? If you accept the paper I presume you will allow me your usual sum, whatever that is for similar contributions—but I set no price—leaving all to your own liberality. The piece will make 8 of your pages and rather more.</p>
    <p>Will you be kind enough to put the best possible interpretation upon my behavior while in N-York? You must have conceived a <i>queer</i> idea of me—but the simple truth is that Fenwick would insist upon <i>the juleps</i>, and I knew not what I was either doing or saying. The Review of Corley which I offered you was deficient in a 1/2 page of commencement, which I had written to supersede the old beginning, and which gave the article the character of a general and retrospective review. No wonder you did not take it—I would have been very much mortified if you had. I hope to see you at some future time, under better auspices.</p>
    <p class="closing">In the meantime I remain<br>Yours very truly,</p>
    <span class="signature" role="img" aria-label="Handwritten signature"></span>
    <p class="signer">Elias Grant</p>
  </div>

  <div class="letter-contact">
    <div class="address">#14 Palm Row, Miami, FL 33101, USA</div>
    <ul>
      <li><svg viewBox="0 0 10 10"><rect x="3" y="0" width="4" height="10" rx="1"/></svg>+1 305 555 0142</li>
      <li><svg viewBox="0 0 10 10"><path d="M0 3 Q5 -1 10 3 L10 5 L7 5 L7 3 L3 3 L3 5 L0 5Z M2 6 H8 V10 H2Z"/></svg>+1 305 555 0177</li>
      <li><svg viewBox="0 0 10 10"><path d="M2 0 H8 V3 H2Z M0 3 H10 V8 H8 V6 H2 V8 H0Z M3 7 H7 V10 H3Z"/></svg>+1 305 555 0176</li>
      <li><svg viewBox="0 0 10 10"><path d="M0 2 H10 V8 H0Z" fill="none" stroke="#e5831a" stroke-width="1.2"/><path d="M0 2 L5 6 L10 2" fill="none" stroke="#e5831a" stroke-width="1.2"/></svg>sales@verdantorchard.com</li>
      <li><svg viewBox="0 0 10 10"><circle cx="5" cy="5" r="5"/></svg>www.verdantorchard.com</li>
    </ul>
  </div>
</section>

<section class="card card-front">
  <div class="brand-name">Verdant Orchard</div>
  <div class="web">www.verdantorchard.com</div>
</section>

<section class="card card-back">
  <svg class="wave" viewBox="0 0 387 215" aria-hidden="true">
    <path d="M0 92 C70 145 150 150 230 100 C290 62 340 55 387 70 L387 215 L0 215Z" fill="var(--orange-soft)"/>
    <path d="M0 94 C70 138 150 140 230 92 C290 58 340 54 387 66 L387 74 C340 60 292 68 236 104 C160 152 72 148 0 100Z" fill="var(--orange)"/>
    <path d="M0 100 C72 148 160 152 236 104 C292 68 340 60 387 74 L387 215 L0 215Z" fill="var(--olive)"/>
  </svg>
  <div class="brand-name">Verdant Orchard</div>
  <div class="address">#14 Palm Row, Miami, FL 33101, USA</div>
  <ul class="contacts">
    <li>+1 305 555 0142<svg viewBox="0 0 10 10"><rect x="3" y="0" width="4" height="10" rx="1"/></svg></li>
    <li>+1 305 555 0177<svg viewBox="0 0 10 10"><path d="M0 3 Q5 -1 10 3 L10 5 L7 5 L7 3 L3 3 L3 5 L0 5Z M2 6 H8 V10 H2Z"/></svg></li>
    <li>+1 305 555 0176<svg viewBox="0 0 10 10"><path d="M2 0 H8 V3 H2Z M0 3 H10 V8 H8 V6 H2 V8 H0Z M3 7 H7 V10 H3Z"/></svg></li>
    <li>sales@verdantorchard.com<svg viewBox="0 0 10 10"><path d="M0 2 H10 V8 H0Z" fill="none" stroke="#e5831a" stroke-width="1.2"/><path d="M0 2 L5 6 L10 2" fill="none" stroke="#e5831a" stroke-width="1.2"/></svg></li>
  </ul>
  <div class="person">
    <div class="name">Marco Ruiz</div>
    <div class="role">CEO</div>
  </div>
</section>

</body>
</html>
```